Bref créative
Bellwether Rheumatology Associates
The Institute for Bone Density
I need double sided standard sized Business Card [3.5" x 2"]
We are flexible, can use different font if looks good.
Professional
Daniel P. Hurlow, MD
Harborview Lakes Medical Center
2716 Kelmont Avenue, Suite 430
Miami Beach, FL 33187
dhurlow1982@mailbrook.example
We are presently a group of two rheumatologists. We are expecting a third rheumatologist the summer of 2012. We will need two versions, one that has my name, Daniel P. Hurlow, MD, and the other that has my partner's name Tomas L. Ferreira Vidal, MD. We are striving for a modern, clean, professional, corporate look. Please use the logo that we are providing. Will be uploading. Would like to keep colors simple. As per logo, we use dark red and gray; I suppose the text on the card will need to be black or similar. Please do NOT put email on card. We still do not have an "official" email. Will also like to see letterhead and envelope design, as well. With the envelope, we are simply looking for a neat-looking, recognizable return address section.
The back of the business card should be the appointment reminder section. Should have a blank for 1. Patient name, 2. Date of appointment 3. Time of appointment 4. Day of week that we can circle (mon-fri only) 5. check box for doctor (either Daniel P. Hurlow, MD or Tomas L. Ferreira Vidal).
Here is the logo.

```html
<!DOCTYPE html>
<html lang="en">
<head>
<meta charset="utf-8">
<title>Bellwether Rheumatology Associates — Stationery</title>
<link rel="stylesheet" href="https://fonts.googleapis.com/css2?family=Cinzel:wght@600&family=Open+Sans:wght@400;600&display=swap">
<style>
  :root {
    --brand-red: #7a1620;
    --rule-red: #8c2a32;
    --ink: #333333;
    --gray: #777777;
    --paper: #ffffff;
    --frame: #dcdcdc;
    --edge: #c9c9c9;
    --watermark: #eee4e1;
  }
  * { margin: 0; padding: 0; box-sizing: border-box; }
  html, body { width: 1200px; height: 681px; overflow: hidden; background: var(--paper); }
  .canvas { position: relative; width: 1200px; height: 681px; font-family: "Open Sans", sans-serif; color: var(--ink); }
  .presentation-frame { position: absolute; left: 12px; top: 12px; width: 1176px; height: 648px; border: 1px solid var(--frame); }

  .sheet { position: absolute; background: var(--paper); border: 1px solid var(--edge); box-shadow: 1px 1px 3px rgba(0,0,0,0.18); }

  .wordmark { position: absolute; display: flex; align-items: flex-start; gap: 6px; }
  .wordmark-square { background: var(--brand-red); flex: none; }
  .wordmark-text { font-family: "Cinzel", serif; font-weight: 600; color: var(--brand-red); line-height: 1.05; text-transform: uppercase; }
  .wordmark-text span { display: block; }

  .return-address { position: absolute; text-align: right; font-size: 7px; line-height: 1.35; color: var(--ink); }
  .red-rule { position: absolute; height: 1px; background: var(--rule-red); }

  /* Envelope front */
  .envelope-front { left: 79px; top: 101px; width: 413px; height: 199px; }
  .envelope-front .wordmark { left: 16px; top: 14px; }
  .envelope-front .wordmark-square { width: 22px; height: 22px; }
  .envelope-front .wordmark-text { font-size: 11px; }
  .envelope-front .wordmark-text .tagline { font-size: 6px; margin-top: 2px; }
  .envelope-front .red-rule { left: 0; right: 0; top: 145px; }
  .envelope-front .return-address { right: 14px; top: 150px; }

  /* Envelope back */
  .envelope-back { left: 79px; top: 336px; width: 413px; height: 204px; }
  .envelope-back svg { position: absolute; left: 0; top: 0; }
  .envelope-back .seal-square { position: absolute; left: 196px; top: 46px; width: 20px; height: 20px; background: var(--brand-red); }

  /* Letterhead */
  .letterhead { left: 612px; top: 48px; width: 384px; height: 588px; }
  .letterhead .wordmark { left: 22px; top: 20px; }
  .letterhead .wordmark-square { width: 30px; height: 30px; }
  .letterhead .wordmark-text { font-size: 16px; }
  .letterhead .wordmark-text .tagline { font-size: 8px; margin-top: 3px; }
  .letterhead .header-rule { left: 22px; right: 22px; top: 62px; opacity: 0.5; }
  .letterhead .watermark { position: absolute; left: 110px; top: 228px; width: 156px; height: 156px; background: var(--watermark); }
  .letterhead .footer-rule { left: 0; right: 0; top: 528px; }
  .letterhead .return-address { right: 14px; top: 534px; }

  /* Business card front */
  .card-front { left: 1003px; top: 228px; width: 173px; height: 91px; }
  .card-front .wordmark { left: 8px; top: 7px; gap: 4px; }
  .card-front .wordmark-square { width: 12px; height: 12px; }
  .card-front .wordmark-text { font-size: 6.5px; }
  .card-front .wordmark-text .tagline { font-size: 4px; margin-top: 1px; }
  .card-front .physician { position: absolute; right: 9px; top: 38px; font-size: 7px; font-weight: 600; color: var(--brand-red); }
  .card-front .return-address { right: 9px; top: 50px; font-size: 4.6px; }
  .card-front .red-rule { left: 0; right: 0; bottom: 9px; }

  /* Business card back */
  .card-back { left: 1003px; top: 336px; width: 173px; height: 115px; font-size: 5px; color: var(--ink); }
  .card-back .form-line { position: absolute; left: 12px; right: 12px; display: flex; align-items: flex-end; gap: 6px; }
  .card-back .form-line .blank { flex: 1; border-bottom: 0.8px solid var(--gray); height: 6px; }
  .card-back .weekdays { position: absolute; left: 12px; top: 64px; display: flex; gap: 7px; }
  .card-back .choice { display: flex; align-items: center; gap: 2px; }
  .card-back .box { width: 5px; height: 5px; border: 0.7px solid var(--gray); }
  .card-back .doctors { position: absolute; left: 12px; top: 82px; display: flex; gap: 8px; font-size: 4.4px; }
</style>
</head>
<body>
<main class="canvas">
  <div class="presentation-frame"></div>

  <section class="sheet envelope-front" aria-label="Envelope front">
    <div class="wordmark">
      <div class="wordmark-square"></div>
      <div class="wordmark-text"><span>Bellwether</span><span>Rheumatology Associates</span><span class="tagline">The Institute for Bone Density</span></div>
    </div>
    <div class="red-rule"></div>
    <address class="return-address">Harborview Lakes Medical Center<br>2716 Kelmont Avenue, Suite 430 | Miami Beach, FL 33187</address>
  </section>

  <section class="sheet envelope-back" aria-label="Envelope back">
    <svg width="413" height="204" viewBox="0 0 413 204" aria-hidden="true">
      <polyline points="0,2 206,100 413,2" fill="none" stroke="#bdbdbd" stroke-width="1"/>
    </svg>
    <div class="seal-square"></div>
  </section>

  <section class="sheet letterhead" aria-label="Letterhead">
    <div class="wordmark">
      <div class="wordmark-square"></div>
      <div class="wordmark-text"><span>Bellwether</span><span>Rheumatology Associates</span><span class="tagline">The Institute for Bone Density</span></div>
    </div>
    <div class="watermark"></div>
    <div class="red-rule footer-rule"></div>
    <address class="return-address">Harborview Lakes Medical Center<br>2716 Kelmont Avenue, Suite 430 | Miami Beach, FL 33187<br>Phone (305) 555-0142 | Fax (305) 555-0187</address>
  </section>

  <section class="sheet card-front" aria-label="Business card front">
    <div class="wordmark">
      <div class="wordmark-square"></div>
      <div class="wordmark-text"><span>Bellwether</span><span>Rheumatology Associates</span><span class="tagline">The Institute for Bone Density</span></div>
    </div>
    <p class="physician">Daniel P. Hurlow, MD</p>
    <address class="return-address">Harborview Lakes Medical Center<br>2716 Kelmont Avenue, Suite 430 | Miami Beach, FL 33187<br>Phone (305) 555-0142 | Fax (305) 555-0187</address>
    <div class="red-rule"></div>
  </section>

  <section class="sheet card-back" aria-label="Appointment reminder">
    <div class="form-line" style="top:14px"><span>Name</span><span class="blank"></span></div>
    <div class="form-line" style="top:30px"><span>Date</span><span class="blank"></span></div>
    <div class="form-line" style="top:46px"><span>Time</span><span class="blank"></span></div>
    <div class="weekdays">
      <span class="choice"><span class="box"></span>Mon</span>
      <span class="choice"><span class="box"></span>Tue</span>
      <span class="choice"><span class="box"></span>Wed</span>
      <span class="choice"><span class="box"></span>Thu</span>
      <span class="choice"><span class="box"></span>Fri</span>
    </div>
    <div class="doctors">
      <span class="choice"><span class="box"></span>Daniel P. Hurlow, MD</span>
      <span class="choice"><span class="box"></span>Tomas L. Ferreira Vidal, MD</span>
    </div>
  </section>
</main>
</body>
</html>
```